Wireless Internet Service Provider website design

We need a Internet Service Provider website that show the packages that we offer as well as the functionality where customers have the option of clicking on the various packages and be linked to a page where they can sign up for our services.
We need about 10-15 pages.
A. Integrated online store.
B. Live chat.
C. Social media page
My old website. Brindlepath.nyc

Example: http://orchardlinkwave.com/services/residential/ Added Tuesday, June 7, 2016

Target Market(s)

Residential and small businesses

Industry/Entity Type

Internet

Coding

Coded - Design and coding required

Number of Pages Required

5+ page

Font styles to use
Serif
Sans Serif
Script

Colors
3176b5
85cae6
ffffff

Requirements
Must have
• Online store and live chat, drop down details on pricing from current website
Nice to have
• great design, functional website,

```html
<!DOCTYPE html>
<html lang="en">
<head>
<meta charset="utf-8">
<title>Brindlepath Wireless</title>
<link rel="stylesheet" href="https://fonts.googleapis.com/css2?family=Roboto:ital,wght@0,300;0,400;0,500;0,700;1,400&display=swap">
<style>
:root{
  --blue:#3176b5;
  --blue-dark:#2a66a0;
  --sky:#85cae6;
  --white:#ffffff;
  --grey-bg:#eef0f3;
  --news-bg:#efefef;
  --text:#555c66;
  --muted:#8a9099;
  --dark:#2b2b2b;
}
*{margin:0;padding:0;box-sizing:border-box}
html,body{width:1200px;height:2871px;overflow:hidden}
body{font-family:'Roboto',sans-serif;color:var(--text);background:var(--white);position:relative}
.abs{position:absolute}
.center{left:0;width:1200px;text-align:center}

/* hero */
.hero{position:absolute;left:0;top:0;width:1200px;height:657px;background:linear-gradient(135deg,#5d96cc 0%,#3f7fbe 45%,#2f6aa8 100%);overflow:hidden}
.hero-photo{position:absolute;left:823px;top:0;width:377px;height:657px;background:linear-gradient(180deg,rgba(60,70,90,.45),rgba(40,50,70,.7))}
.topbar{position:absolute;top:20px;left:88px;display:flex;gap:34px;align-items:center;color:var(--white);font-size:18px}
.topbar .signup{font-size:16px;font-weight:500;display:flex;align-items:center;gap:8px}
.brand-oval{position:absolute;left:364px;top:96px;width:471px;height:330px;border-radius:50%;background:var(--white);border:4px solid #a9d6ef;display:flex;flex-direction:column;align-items:center;justify-content:center;gap:22px}
.brand-dot{width:70px;height:70px;border-radius:50%;background:var(--blue)}
.brand-name{font-size:38px;font-weight:500;color:#5a6470}
.nav{position:absolute;left:0;top:593px;width:1200px;height:64px;border-top:1px solid rgba(255,255,255,.35);background:rgba(30,80,140,.35)}
.nav a{position:absolute;top:22px;color:var(--white);font-size:16px;text-decoration:none;text-transform:uppercase}
.nav a.active{color:#b9def2}
.nav .marker{position:absolute;left:157px;top:-2px;width:80px;height:3px;background:#b9def2}

/* welcome */
.welcome-mark{left:582px;top:712px;width:36px;height:36px;border-radius:50%;background:var(--blue)}
.h2{font-size:42px;font-weight:400;color:var(--blue);text-transform:uppercase}
.h2 span{color:var(--sky)}
.lead{left:160px;width:880px;text-align:center;font-size:15px;line-height:27px;color:var(--muted)}
.btn{background:var(--blue);color:var(--white);font-size:20px;text-transform:uppercase;display:flex;align-items:center;justify-content:center}

/* plans */
.plans{left:0;top:1133px;width:1200px;height:662px;background:var(--grey-bg)}
.tabs{left:279px;top:1285px;width:642px;height:42px;border-bottom:2px solid var(--blue);display:flex;font-size:19px}
.tabs div{flex:1;text-align:center}
.tabs .on{color:var(--blue)}
.tabs .off{color:#444;border-left:1px solid #ccc}
.card{background:var(--white);text-align:center}
.price{width:114px;height:114px;border-radius:50%;background:var(--blue);color:var(--white);font-size:30px;line-height:32px;display:flex;flex-direction:column;align-items:center;justify-content:center}
.term{font-size:17px;font-style:italic;color:#3aa2d6}
.plan-name{font-size:21px;color:#333}
.card-feat{background:var(--blue);color:var(--white);text-align:center;box-shadow:0 6px 10px rgba(0,0,0,.25)}

/* about */
.feature-icon{width:104px;height:104px;border-radius:50%;border:4px solid var(--blue);display:flex;align-items:center;justify-content:center}
.feature-title{font-size:19px;color:#333;text-transform:uppercase;text-align:center;width:360px}
.feature-text{font-size:15px;line-height:25px;color:var(--muted);text-align:center;width:340px}

/* newsletter */
.newsletter{left:0;top:2264px;width:1200px;height:253px;background:var(--news-bg)}
.email-input{left:304px;top:2425px;width:416px;height:48px;background:var(--white);border:1px solid #d5d5d5;font-size:15px;color:#777;padding:14px 14px}

/* footer */
.footer{left:0;top:2517px;width:1200px;height:354px;background:var(--blue);color:var(--white)}
.f-head{font-size:17px;font-weight:700;text-transform:uppercase}
.feed-dot{width:44px;height:44px;border-radius:50%;background:var(--white)}
.feed-text{font-size:14px;line-height:24px;color:#dbe9f6}
.contact-line{font-size:15px;color:#dbe9f6}
.social{width:36px;height:36px;border-radius:50%;border:2px solid var(--white)}
.social.fill{background:var(--white)}
.copyright{font-size:14px;color:#1d2a38}
.email-tab{left:980px;top:2833px;width:145px;height:38px;background:#2b2b2b;color:var(--white);font-size:17px;display:flex;align-items:center;justify-content:center;gap:8px}
</style>
</head>
<body>

<header class="hero">
  <div class="hero-photo" role="img" aria-label="Smiling businessman in a suit holding an open laptop"></div>
  <div class="topbar">
    <span>
      <svg width="20" height="18" viewBox="0 0 20 18" style="vertical-align:-2px;margin-right:10px"><path d="M0 1h4l3 10h10l2-7H6" fill="none" stroke="#fff" stroke-width="2"/><circle cx="8" cy="15" r="1.8" fill="#fff"/><circle cx="16" cy="15" r="1.8" fill="#fff"/></svg>Shopping cart 0</span>
    <span class="signup">SIGN UP
      <svg width="22" height="18" viewBox="0 0 22 18"><path d="M1 9h11M8 4l5 5-5 5" fill="none" stroke="#fff" stroke-width="2.5"/><path d="M14 1h6v16h-6" fill="none" stroke="#fff" stroke-width="2.5"/></svg></span>
  </div>
  <div class="brand-oval">
    <div class="brand-dot"></div>
    <div class="brand-name">Brindlepath Wireless</div>
  </div>
  <nav class="nav">
    <span class="marker"></span>
    <a class="active" style="left:174px">Home</a>
    <a style="left:278px">Why Brindlepath</a>
    <a style="left:446px">Plans &amp; Packages</a>
    <a style="left:658px">My Account</a>
    <a style="left:818px">Gallery</a>
    <a style="left:951px">Contact</a>
  </nav>
</header>

<section class="welcome">
  <div class="abs welcome-mark"></div>
  <h2 class="abs center h2" style="top:770px">Welcome to <span>Brindlepath Wireless</span></h2>
  <p class="abs lead" style="top:828px">Brindlepath wireless is a highly reputable company, which is aiming at providing high quality internet access and phone services to a market that is continually growing. We are dedicated to filling the digital gap that has been created in the middle and lowe. Brindlepath offers high speed internet to meet your needs at an affordable price.</p>
  <p class="abs lead" style="top:912px">Finally the internet that you have been waiting for is only a click away. With Brindlepath you get your money's. Brindlepath offers high speed internet to meet your needs at an affordable price. Finally the internet that you have been waiting for is only a click away. With Brindlepath you get your money's worth with no hidden fees like the big cable company's</p>
  <div class="abs btn" style="left:505px;top:1020px;width:188px;height:61px">Sign up now</div>
</section>

<section class="abs plans"></section>
<h2 class="abs center h2" style="top:1190px">Our Plans <span>&amp; Packages</span></h2>
<div class="abs tabs"><div class="on">Residential Internet Access</div><div class="off">Business Internet Access</div></div>

<div class="abs card" style="left:78px;top:1416px;width:249px;height:312px"></div>
<div class="abs price" style="left:145px;top:1359px"><span>$</span><span>39.99</span></div>
<div class="abs term" style="left:78px;top:1508px;width:249px;text-align:center">Mo/1 Year</div>
<div class="abs plan-name" style="left:78px;top:1554px;width:249px;text-align:center">Brindlepath Simplicity</div>
<div class="abs btn" style="left:117px;top:1608px;width:170px;height:56px">Know more</div>

<div class="abs card" style="left:345px;top:1416px;width:248px;height:312px"></div>
<div class="abs price" style="left:412px;top:1359px"><span>$</span><span>49.95</span></div>
<div class="abs term" style="left:345px;top:1502px;width:248px;text-align:center">Mo/1 Year</div>
<div class="abs plan-name" style="left:345px;top:1550px;width:248px;text-align:center">Brindlepath Value Pak</div>
<div class="abs btn" style="left:384px;top:1604px;width:170px;height:56px">Know more</div>

<div class="abs card-feat" style="left:609px;top:1416px;width:248px;height:316px"></div>
<div class="abs" style="left:674px;top:1356px;width:118px;height:118px;border-radius:50%;background:#fff;border:3px solid var(--blue);display:flex;align-items:center;justify-content:center">
  <svg width="48" height="48" viewBox="0 0 48 48" fill="none" stroke="#3aa2d6" stroke-width="2"><circle cx="24" cy="24" r="5"/><circle cx="24" cy="6" r="3"/><circle cx="24" cy="42" r="3"/><circle cx="6" cy="24" r="3"/><circle cx="42" cy="24" r="3"/><path d="M24 9v10M24 29v10M9 24h10M29 24h10"/></svg>
</div>
<div class="abs" style="left:609px;top:1488px;width:248px;text-align:center;color:#fff;font-size:30px">$89.99</div>
<div class="abs" style="left:609px;top:1530px;width:248px;text-align:center;color:#fff;font-size:23px;font-style:italic;line-height:32px">50 Mbps Download<br>Speed</div>
<div class="abs" style="left:619px;top:1598px;width:228px;text-align:center;color:#e4effa;font-size:14px;line-height:26px">With super-fast download speeds of 50 Mbps, this is the all-in plan for anyone whose..</div>
<svg class="abs" style="left:721px;top:1690px" width="24" height="22" viewBox="0 0 24 22" fill="none" stroke="#fff" stroke-width="2.5"><path d="M3 2l9 8 9-8M3 11l9 8 9-8"/></svg>

<div class="abs card" style="left:873px;top:1416px;width:249px;height:312px"></div>
<div class="abs price" style="left:940px;top:1359px"><span>$</span><span>69.99</span></div>
<div class="abs term" style="left:873px;top:1504px;width:249px;text-align:center">Mo/1 Year</div>
<div class="abs plan-name" style="left:873px;top:1550px;width:249px;text-align:center">Brindlepath Super- Pak</div>
<div class="abs btn" style="left:912px;top:1604px;width:170px;height:56px">Know more</div>

<section class="about">
  <h2 class="abs center h2" style="top:1855px">About <span>Brindlepath Wireless</span></h2>
  <p class="abs lead" style="left:370px;width:460px;top:1910px">Brindlepath wireless is a highly reputable company, which is aiming at providing high quality internet access...</p>

  <div class="abs feature-icon" style="left:185px;top:1986px">
    <svg width="54" height="54" viewBox="0 0 54 54"><circle cx="27" cy="27" r="25" fill="#3aa2d6"/><circle cx="27" cy="25" r="11" fill="#fff"/><path d="M12 25a15 15 0 0 1 30 0" fill="none" stroke="#fff" stroke-width="3"/><rect x="9" y="23" width="5" height="9" rx="2" fill="#fff"/><rect x="40" y="23" width="5" height="9" rx="2" fill="#fff"/></svg>
  </div>
  <div class="abs feature-title" style="left:57px;top:2108px">Customer Support Center</div>
  <p class="abs feature-text" style="left:67px;top:2138px">Reliable and Amicable Customer Support Services at Your Doorstep 24/7, 365</p>

  <div class="abs feature-icon" style="left:547px;top:1986px">
    <svg width="50" height="50" viewBox="0 0 50 50"><g fill="var(--blue)"><circle cx="25" cy="25" r="15"/><rect x="21" y="3" width="8" height="44" rx="2"/><rect x="3" y="21" width="44" height="8" rx="2"/><rect x="21" y="3" width="8" height="44" rx="2" transform="rotate(45 25 25)"/><rect x="21" y="3" width="8" height="44" rx="2" transform="rotate(-45 25 25)"/></g><circle cx="25" cy="25" r="6" fill="#fff"/></svg>
  </div>
  <div class="abs feature-title" style="left:419px;top:2108px">Equipment Options</div>
  <p class="abs feature-text" style="left:429px;top:2138px">a built-in 4-port full-duplex 10/100 switch to connect your devices together</p>

  <div class="abs feature-icon" style="left:918px;top:1986px">
    <svg width="52" height="52" viewBox="0 0 52 52"><circle cx="26" cy="26" r="25" fill="#3aa2d6"/><path d="M14 24h6v14h-6zM22 24l6-10c2-2 5-1 4 3l-1 5h8c2 0 3 2 2 4l-3 10c-1 2-2 2-4 2H22z" fill="#fff"/></svg>
  </div>
  <div class="abs feature-title" style="left:790px;top:2108px">Customer Guarantee</div>
  <p class="abs feature-text" style="left:800px;top:2138px">Unlimited internet usage, you pay to get internet access so use your internet to do what you want.</p>
</section>

<section class="abs newsletter"></section>
<h2 class="abs center h2" style="top:2300px">Newsletter</h2>
<p class="abs lead" style="left:285px;width:630px;top:2357px">Lorem Ipsum is simply dummy text of the printing and typesetting industry. Lorem Ipsum has been the dummy text of the printing.</p>
<div class="abs email-input">Enter your Email Id</div>
<div class="abs btn" style="left:731px;top:2425px;width:165px;height:48px">Subscribe</div>

<footer class="abs footer"></footer>
<div class="abs f-head" style="left:78px;top:2551px;color:#fff">Social Feed</div>
<div class="abs feed-dot" style="left:76px;top:2598px"></div>
<div class="abs feed-text" style="left:135px;top:2596px;width:200px">Lorem ipsum is simple dummy text of print and Type..<br>Today 1:45 pm - 0.06.2016</div>
<div class="abs feed-text" style="left:357px;top:2596px">5m ago</div>
<div class="abs feed-dot" style="left:76px;top:2686px"></div>
<div class="abs feed-text" style="left:135px;top:2684px;width:200px">Lorem ipsum is simple dummy text of print and Type..<br>Today 1:45 pm - 0.06.2016</div>
<div class="abs feed-text" style="left:357px;top:2684px">2h ago</div>

<div class="abs" style="left:565px;top:2590px;width:70px;height:70px;border-radius:50%;background:#fff"></div>
<div class="abs" style="left:400px;top:2714px;width:400px;text-align:center;color:#fff;font-size:30px;font-weight:500">Brindlepath Wireless</div>

<div class="abs f-head" style="left:802px;top:2551px;color:#fff">Get in touch</div>
<svg class="abs" style="left:800px;top:2600px" width="16" height="20" viewBox="0 0 16 20" fill="none" stroke="#fff" stroke-width="1.6"><path d="M8 19s6-7 6-11A6 6 0 0 0 2 8c0 4 6 11 6 11z"/><circle cx="8" cy="8" r="2"/></svg>
<div class="abs contact-line" style="left:838px;top:2601px;line-height:28px">BRINDLEPATH WIRELESS<br>P O Box 40117 Brooklyn NY 11201</div>
<svg class="abs" style="left:799px;top:2663px" width="18" height="18" viewBox="0 0 18 18" fill="none" stroke="#fff" stroke-width="1.6"><path d="M3 1l3 4-2 2c1 3 4 6 7 7l2-2 4 3-2 2C9 17 1 9 1 3z"/></svg>
<div class="abs contact-line" style="left:838px;top:2662px">555-014-2290</div>
<svg class="abs" style="left:799px;top:2702px" width="18" height="18" viewBox="0 0 18 18" fill="none" stroke="#fff" stroke-width="1.6"><path d="M1 8l16-7-6 16-3-6zM8 11l9-10"/></svg>
<div class="abs contact-line" style="left:838px;top:2702px">support@brindlepath.nyc</div>
<div class="abs social fill" style="left:836px;top:2739px"></div>
<div class="abs social" style="left:883px;top:2739px"></div>
<div class="abs social" style="left:929px;top:2739px"></div>

<div class="abs" style="left:78px;top:2810px;width:1044px;height:1px;background:rgba(255,255,255,.3)"></div>
<div class="abs center copyright" style="top:2831px">©<b>BRINDLEPATH WIRELESS</b> - 2016 All rights reserved.</div>
<div class="abs email-tab">
  <svg width="18" height="16" viewBox="0 0 18 16" fill="#fff"><path d="M0 1h12v8H5l-3 3V9H0zM14 4h4v8h-2v3l-3-3H7v-1h7z"/></svg>Email us
</div>

</body>
</html>
```